Flu Vaccination Poster

I would like a banner designed to display from the ceiling in my pharmacy promoting flu vaccination.
In large words, it should say "Flu Vaccination"
In smaller text it should say "Available here. See in store for details"
It should also display our website riverbendchemist.com.au and have a message for more information visit the website.
Currently patients required to pay for the service, however in May this year the vaccine will become free for everyone, so I would like to put a sticker on the sign in May saying "FREE" and then remove the sticker when no longer free. The banner dimensions are "2.19m wide x 0.61m tall.
I have uploaded logo files plus a photo of a previously used banner which is no longer relevant. More formats of logo files are available if required.

```html
<!DOCTYPE html>
<html lang="en">
<head>
<meta charset="utf-8">
<title>Flu Vaccination Banner – Riverbend Chemist</title>
<link href="https://fonts.googleapis.com/css2?family=Inter:wght@500;900&family=Source+Sans+3:wght@400;700;800&family=Anton&display=swap" rel="stylesheet">
<style>
  :root {
    --backdrop: #c4c4c4;
    --banner-white: #ffffff;
    --navy: #243d66;
    --subline-blue: #1f4f92;
    --accent-blue: #1b5aa6;
    --url-blue: #a8cbe9;
    --sticker-pink: #d91a63;
    --sticker-text: #ffffff;
  }
  * { margin: 0; padding: 0; box-sizing: border-box; }
  html, body {
    width: 1200px;
    height: 754px;
    overflow: hidden;
    background: var(--backdrop);
  }
  .banner {
    position: absolute;
    left: 99px;
    width: 1001px;
    height: 279px;
    background: var(--banner-white);
    overflow: visible;
  }
  .banner--standard { top: 64px; }
  .banner--free { top: 400px; }

  .headline {
    position: absolute;
    top: 40px;
    left: 0;
    width: 100%;
    text-align: center;
    font-family: "Inter", sans-serif;
    font-size: 100px;
    line-height: 1;
    letter-spacing: -1px;
    color: var(--navy);
    white-space: nowrap;
  }
  .headline__flu { font-weight: 900; letter-spacing: -3px; }
  .headline__vaccination { font-weight: 500; }

  .subline {
    position: absolute;
    top: 140px;
    left: 0;
    width: 100%;
    text-align: center;
    font-family: "Source Sans 3", sans-serif;
    font-size: 48px;
    line-height: 1;
    letter-spacing: -1px;
    color: var(--subline-blue);
    font-weight: 400;
    white-space: nowrap;
  }
  .subline__emphasis {
    font-weight: 800;
    color: var(--accent-blue);
    letter-spacing: -1.5px;
  }

  .web-band {
    position: absolute;
    left: 0;
    bottom: 0;
    width: 100%;
    height: 71px;
    background: var(--navy);
    display: flex;
    align-items: center;
    justify-content: center;
  }
  .web-band__url {
    font-family: "Source Sans 3", sans-serif;
    font-weight: 700;
    font-size: 26px;
    letter-spacing: -0.3px;
    color: var(--url-blue);
  }

  .free-sticker {
    position: absolute;
    left: 27px;
    top: 152px;
    width: 114px;
    height: 114px;
    border-radius: 50%;
    background: var(--sticker-pink);
    display: flex;
    align-items: center;
    justify-content: center;
    font-family: "Anton", sans-serif;
    font-size: 50px;
    line-height: 1;
    color: var(--sticker-text);
    letter-spacing: -0.5px;
    z-index: 2;
  }
</style>
</head>
<body>
  <section class="banner banner--standard">
    <h1 class="headline"><span class="headline__flu">FLU</span> <span class="headline__vaccination">VACCINATION</span></h1>
    <p class="subline">Available here. <span class="subline__emphasis">See in store</span> for details</p>
    <div class="web-band"><span class="web-band__url">www.riverbendchemist.com.au</span></div>
  </section>

  <section class="banner banner--free">
    <h1 class="headline"><span class="headline__flu">FLU</span> <span class="headline__vaccination">VACCINATION</span></h1>
    <p class="subline">Available here. <span class="subline__emphasis">See in store</span> for details</p>
    <div class="web-band"><span class="web-band__url">www.riverbendchemist.com.au</span></div>
    <div class="free-sticker">FREE</div>
  </section>
</body>
</html>
```